Business Card & Stationary
Harbor Lane Finanical
Project: Business Card & Stationary
Business Card & Stationary - Financial Services
Creative Brief
Simple
Gordon Pelling
President
274 W. Larkspur Blvd. Suite 2260 Chicago, IL 60614
gpelling@harborlanefin.com
www.harborlanefin.com
The stationary should also be converted into a template for Word. We will get the business cards and envelopes printed but probably just use a laser printer for the stationary.
Some element of our logo .... make it look nice.

```html
<!DOCTYPE html>
<html lang="en">
<head>
<meta charset="utf-8">
<title>Harbor Lane Finanical — Stationery</title>
<link rel="stylesheet" href="https://fonts.googleapis.com/css2?family=Cinzel:wght@500&family=Lato:wght@400;700&display=swap">
<style>
  :root {
    --backdrop: #d9d9d9;
    --paper: #ffffff;
    --paper-edge: #e4e4e4;
    --brand-green: #6b7d2c;
    --ink: #4a4a4a;
    --ink-soft: #8a8a8a;
    --on-green: #ffffff;
  }
  * { box-sizing: border-box; margin: 0; padding: 0; }
  html, body { width: 1200px; height: 706px; overflow: hidden; }
  body {
    background: var(--backdrop);
    font-family: "Lato", Arial, sans-serif;
    color: var(--ink);
    position: relative;
  }
  address { font-style: normal; }
  .sheet {
    position: absolute;
    background: var(--paper);
    border: 1px solid var(--paper-edge);
  }
  .brand { display: flex; align-items: center; gap: 7px; }
  .brand-square { background: var(--brand-green); flex: none; }
  .brand-name {
    font-family: "Cinzel", "Times New Roman", serif;
    font-weight: 500;
    color: var(--brand-green);
    text-transform: uppercase;
    letter-spacing: .05em;
    white-space: nowrap;
  }
  .fine { font-size: 6px; line-height: 1.55; color: var(--ink-soft); white-space: nowrap; }

  /* Letterheads */
  .letterhead { top: 50px; width: 360px; height: 466px; }
  .letterhead-first { left: 250px; }
  .letterhead-second { left: 640px; }
  .letterhead .brand { position: absolute; left: 30px; top: 40px; }
  .letterhead .brand-square { width: 16px; height: 16px; }
  .letterhead .brand-name { font-size: 9.5px; }
  .letterhead .header-contact { position: absolute; left: 236px; top: 32px; }
  .letterhead .footer-web { position: absolute; left: 0; right: 0; bottom: 14px; text-align: center; }
  .letterhead .footer-contact { position: absolute; left: 0; right: 0; bottom: 12px; text-align: center; }

  /* Envelope */
  .envelope { left: 790px; top: 300px; width: 370px; height: 165px; }
  .envelope .brand { position: absolute; left: 24px; top: 52px; }
  .envelope .brand-square { width: 16px; height: 16px; }
  .envelope .brand-name { font-size: 9.5px; }
  .envelope .return-address { position: absolute; left: 24px; top: 74px; }

  /* Business cards */
  .card { left: 24px; width: 210px; height: 124px; border-radius: 8px; overflow: hidden; }
  .card-front { top: 330px; }
  .card-front .brand { position: absolute; left: 14px; top: 16px; }
  .card-front .brand-square { width: 14px; height: 14px; }
  .card-front .brand-name { font-size: 9px; }
  .card-front .name-band {
    position: absolute; left: 0; right: 0; top: 44px; height: 17px;
    background: var(--brand-green); color: var(--on-green);
    font-size: 7px; padding: 4px 14px; letter-spacing: .04em;
  }
  .card-front .card-contact { position: absolute; left: 14px; top: 68px; }
  .card-back { top: 478px; }
  .card-back .brand { position: absolute; left: 0; right: 0; top: 38px; justify-content: center; }
  .card-back .brand-square { width: 26px; height: 26px; }
  .card-back .brand-name { font-size: 9px; }
  .card-back .card-web { position: absolute; left: 0; right: 0; bottom: 12px; text-align: center; }
</style>
</head>
<body>

<section class="sheet letterhead letterhead-first" aria-label="Letterhead, first page">
  <div class="brand"><span class="brand-square"></span><span class="brand-name">Harbor Lane Finanical</span></div>
  <address class="header-contact fine">
    274 W. Larkspur Blvd.<br>Suite 2260 Chicago, IL 60614<br>t +1 (312) 555-0142<br>f +1 (312) 555-0143
  </address>
  <p class="footer-web fine">www.harborlanefin.com</p>
</section>

<section class="sheet letterhead letterhead-second" aria-label="Letterhead, second page">
  <div class="brand"><span class="brand-square"></span><span class="brand-name">Harbor Lane Finanical</span></div>
  <address class="header-contact fine">
    274 W. Larkspur Blvd.<br>Suite 2260 Chicago, IL 60614<br>t +1 (312) 555-0142<br>f +1 (312) 555-0143
  </address>
  <p class="footer-contact fine">274 W. Larkspur Blvd. Suite 2260 Chicago, IL 60614<br>t +1 (312) 555-0142 &nbsp; f +1 (312) 555-0143 &nbsp; www.harborlanefin.com</p>
</section>

<section class="sheet envelope" aria-label="Envelope">
  <div class="brand"><span class="brand-square"></span><span class="brand-name">Harbor Lane Finanical</span></div>
  <p class="return-address fine">274 W. Larkspur Blvd. Suite 2260 Chicago, IL 60614</p>
</section>

<section class="sheet card card-front" aria-label="Business card, front">
  <div class="brand"><span class="brand-square"></span><span class="brand-name">Harbor Lane Finanical</span></div>
  <p class="name-band"><strong>Gordon Pelling</strong> | President</p>
  <p class="card-contact fine">274 W. Larkspur Blvd. Suite 2260 Chicago, IL 60614<br>t +1 (312) 555-0142 &nbsp; f +1 (312) 555-0143<br>gpelling@harborlanefin.com</p>
</section>

<section class="sheet card card-back" aria-label="Business card, back">
  <div class="brand"><span class="brand-square"></span><span class="brand-name">Harbor Lane Finanical</span></div>
  <p class="card-web fine">www.harborlanefin.com</p>
</section>

</body>
</html>
```